Sign Design

We already have a logo, but would like to design 2 x signs.
Sign 1:
Dimensions 1500mm wide x 2500m high.
Information to include on sign: - Clinic name and logo (attached)
- the word "DENTIST "
- Street number (which is 348)
Phone number (which is 6153 4097)

Sign 2:
Dimensions: 800mm wide x 600mm high

```html
<!DOCTYPE html>
<html lang="en">
<head>
<meta charset="utf-8">
<title>Brookfield Dental Care – Dentist Sign</title>
<link rel="stylesheet" href="https://fonts.googleapis.com/css2?family=Bebas+Neue&family=Open+Sans:ital,wght@0,400;0,600;1,700&display=swap">
<style>
  :root {
    --page-bg: #dcebfb;
    --sign-white: #f7fbfe;
    --sky-wave: #d9e9fb;
    --green-light: #a2cf4f;
    --green-mid: #86bd38;
    --green-deep: #6aa82a;
    --brand-dark: #1d6a35;
    --headline: #93c445;
    --body-text: #2f5d3f;
    --white: #ffffff;
  }
  * { margin: 0; padding: 0; box-sizing: border-box; }
  html, body { width: 1200px; height: 773px; overflow: hidden; }
  body {
    background: var(--page-bg);
    display: flex;
    align-items: center;
    justify-content: center;
    font-family: "Open Sans", Arial, sans-serif;
  }
  .sign {
    position: relative;
    width: 423px;
    height: 700px;
    background: var(--sign-white);
    box-shadow: 0 8px 28px rgba(40, 70, 110, 0.35);
    overflow: hidden;
  }
  .sign-waves { position: absolute; inset: 0; width: 100%; height: 100%; }
  .brand {
    position: absolute;
    top: 78px;
    left: 0; right: 0;
    display: flex;
    align-items: center;
    justify-content: center;
    gap: 14px;
  }
  .brand-dot {
    width: 52px; height: 52px;
    border-radius: 50%;
    background: var(--green-mid);
  }
  .brand-name {
    font-family: "Open Sans", Arial, sans-serif;
    font-weight: 600;
    font-size: 27px;
    line-height: 1.05;
    color: var(--brand-dark);
  }
  .headline {
    position: absolute;
    top: 176px; left: 0; right: 0;
    text-align: center;
    font-family: "Bebas Neue", Impact, sans-serif;
    font-size: 76px;
    line-height: 1;
    letter-spacing: 1px;
    color: var(--headline);
  }
  .question {
    position: absolute;
    top: 249px; left: 0; right: 0;
    text-align: center;
    font-style: italic;
    font-weight: 700;
    font-size: 17px;
    color: var(--brand-dark);
  }
  .intro {
    position: absolute;
    top: 282px; left: 40px; right: 40px;
    text-align: center;
    font-size: 15.5px;
    line-height: 22px;
    color: var(--body-text);
  }
  .contact {
    position: absolute;
    left: 0; right: 0;
    display: flex;
    align-items: center;
    justify-content: center;
    gap: 10px;
    color: var(--white);
    font-family: "Bebas Neue", Impact, sans-serif;
  }
  .contact-phone { top: 472px; font-size: 62px; line-height: 1; letter-spacing: 2px; }
  .contact-email { top: 544px; font-size: 19px; letter-spacing: 1.5px; line-height: 1; }
  .contact-pin { top: 585px; }
  .contact-street { top: 619px; font-size: 22px; letter-spacing: 1.5px; line-height: 1; }
  .icon { fill: var(--white); display: block; }
</style>
</head>
<body>
  <main class="sign">
    <svg class="sign-waves" viewBox="0 0 527 873" preserveAspectRatio="none" aria-hidden="true">
      <defs>
        <linearGradient id="greenFill" x1="0" y1="0" x2="0" y2="1">
          <stop offset="0" stop-color="#a6d353"/>
          <stop offset="0.55" stop-color="#8cc23c"/>
          <stop offset="1" stop-color="#6ea82c"/>
        </linearGradient>
      </defs>
      <path fill="#d9e9fb" d="M0 498 C 90 470 170 500 250 470 C 320 440 360 410 410 420 C 470 432 505 480 527 540 L527 873 L0 873 Z"/>
      <path fill="url(#greenFill)" d="M0 590 C 20 545 60 530 100 536 C 150 544 180 565 225 555 C 280 540 320 470 385 466 C 450 462 505 530 527 640 L527 873 L0 873 Z"/>
    </svg>

    <header class="brand">
      <span class="brand-dot"></span>
      <span class="brand-name">Brookfield<br>Dental Care</span>
    </header>

    <h1 class="headline">Dentist</h1>
    <p class="question">What is Lorem Ipsum?</p>
    <p class="intro">Lorem Ipsum is simply dummy text of the nting and typesetting industry.</p>

    <div class="contact contact-phone">
      <svg class="icon" width="44" height="44" viewBox="0 0 24 24" aria-hidden="true"><path d="M6.6 10.8a15.1 15.1 0 0 0 6.6 6.6l2.2-2.2c.3-.3.7-.4 1-.2 1.1.4 2.3.6 3.6.6.6 0 1 .4 1 1V20c0 .6-.4 1-1 1A17 17 0 0 1 3 4c0-.6.4-1 1-1h3.5c.6 0 1 .4 1 1 0 1.3.2 2.5.6 3.6.1.3 0 .7-.2 1z"/></svg>
      <span>6153 4097</span>
    </div>

    <div class="contact contact-email">
      <svg width="30" height="22" viewBox="0 0 30 22" aria-hidden="true"><rect x="1.5" y="1.5" width="27" height="19" fill="none" stroke="#fff" stroke-width="2.2"/><path d="M1.5 1.5 L15 12 L28.5 1.5 M1.5 20.5 L11 10 M28.5 20.5 L19 10" fill="none" stroke="#fff" stroke-width="2.2"/></svg>
      <span>WWW.HELLO@BROOKFIELDSMILE.COM</span>
    </div>

    <div class="contact contact-pin">
      <svg class="icon" width="20" height="28" viewBox="0 0 20 28" aria-hidden="true"><path d="M10 0C4.5 0 0 4.4 0 9.8 0 17 10 28 10 28s10-11 10-18.2C20 4.4 15.5 0 10 0zm0 14a4.2 4.2 0 1 1 0-8.4 4.2 4.2 0 0 1 0 8.4z"/></svg>
    </div>

    <div class="contact contact-street"><span>STREET NUMBER 348</span></div>
  </main>
</body>
</html>
```